design business card

We are a new Auto Parts company that selling parts online on website and via mobile apps for android and ios .

We looking to create new business card template for our mangers and agents- same card template .

Our company name is : Zip Wheel - Auto parts and services

**logo attached

****************************************************************************************
We need on the business card the following information :

create your designs in English - from left to right .
or create your designs in Hebrew- from right to left with the following info ( the text direction and design should be from right to left) - like in Arabic

Zip Wheel logo
Auto parts and services = שירותים וחלפים לרכב

Name - אורי מלכה
Role : סוכן מכירות
Phone
ori@zip-wheel.co.il
Website Address : [login to view URL] .
Main warehouse Address - הדקל 42, חיפה

And use the colorful icons

Note :

we want to get the design as a template so we can create cards for our new agents in the future .

thank you !

```html
<!DOCTYPE html>
<html lang="he">
<head>
<meta charset="utf-8">
<title>Zip Wheel – business card</title>
<link href="https://fonts.googleapis.com/css2?family=Heebo:wght@400;500;700;800&display=swap" rel="stylesheet">
<style>
  :root {
    --bg: #6a6a6c;
    --blue: #4f80c4;
    --blue-deep: #3b4f9f;
    --blue-light: #6ca6dd;
    --white: #ffffff;
    --ink: #1f2a44;
    --badge: #1d1d22;
  }
  * { margin: 0; padding: 0; box-sizing: border-box; }
  html, body { width: 1200px; height: 799px; overflow: hidden; }
  body {
    background: var(--bg);
    font-family: "Heebo", sans-serif;
    position: relative;
  }
  .card {
    position: absolute;
    top: 245px;
    width: 520px;
    height: 310px;
    background: var(--white);
    overflow: hidden;
    border-radius: 4px;
  }
  .card-back { left: 50px; }
  .card-front { left: 630px; }

  /* back side */
  .back-band-top { position: absolute; left: 0; top: 0; width: 100%; height: 62px; background: var(--blue); }
  .back-band-bottom { position: absolute; left: 0; bottom: 0; width: 100%; height: 105px; background: var(--blue); }
  .brand {
    font-family: "Heebo", sans-serif;
    font-weight: 800;
    color: var(--blue);
    letter-spacing: 0.5px;
    display: flex;
    align-items: center;
    gap: 10px;
    white-space: nowrap;
  }
  .brand-dot { width: 0.8em; height: 0.8em; border-radius: 50%; background: var(--blue); }
  .back-brand { position: absolute; top: 86px; left: 0; width: 100%; justify-content: center; font-size: 40px; }
  .store-badges { position: absolute; left: 26px; bottom: 22px; display: flex; flex-direction: column; gap: 10px; }
  .store-badge { width: 86px; height: 24px; border-radius: 4px; background: var(--badge); border: 1px solid #8a8a8a; }

  /* front side */
  .front-art { position: absolute; inset: 0; }
  .front-brand { position: absolute; right: 34px; top: 96px; font-size: 42px; }
  .holder {
    position: absolute;
    right: 360px;
    top: 46px;
    text-align: right;
    color: var(--white);
    direction: rtl;
    white-space: nowrap;
  }
  .holder-name { font-size: 24px; font-weight: 500; line-height: 1.2; }
  .holder-role { font-size: 15px; font-weight: 400; line-height: 1.35; }
  .holder-tagline { font-size: 12px; font-weight: 400; line-height: 1.35; opacity: 0.9; }
  .contacts { position: absolute; left: 0; top: 188px; list-style: none; }
  .contact { display: flex; align-items: center; height: 28px; }
  .contact-icon { width: 30px; height: 28px; background: var(--blue-deep); display: flex; align-items: center; justify-content: center; }
  .contact-text { margin-left: 10px; font-size: 12.5px; color: var(--ink); white-space: nowrap; }
</style>
</head>
<body>

  <section class="card card-back" aria-label="Card back">
    <div class="back-band-top"></div>
    <div class="brand back-brand"><span class="brand-dot"></span>Zip Wheel</div>
    <div class="back-band-bottom">
      <div class="store-badges">
        <div class="store-badge" role="img" aria-label="App store badge"></div>
        <div class="store-badge" role="img" aria-label="App store badge"></div>
      </div>
    </div>
  </section>

  <section class="card card-front" aria-label="Card front">
    <svg class="front-art" viewBox="0 0 520 310" width="520" height="310" aria-hidden="true">
      <polygon points="0,0 200,0 150,148 330,310 0,310" fill="var(--blue)"/>
      <g stroke-width="9" fill="none">
        <polyline points="214,0 164,148 342,310" stroke="var(--white)"/>
        <polyline points="226,0 176,148 356,310" stroke="var(--blue-light)"/>
        <polyline points="240,0 190,148 372,310" stroke="var(--blue)"/>
        <polyline points="254,0 204,148 388,310" stroke="var(--blue-deep)"/>
      </g>
    </svg>

    <div class="holder">
      <div class="holder-name">אורי מלכה</div>
      <div class="holder-role">סוכן מכירות</div>
      <div class="holder-tagline">שירותים וחלפים לרכב</div>
    </div>

    <div class="brand front-brand"><span class="brand-dot"></span>Zip Wheel</div>

    <ul class="contacts">
      <li class="contact">
        <span class="contact-icon">
          <svg width="15" height="15" viewBox="0 0 24 24" fill="none" stroke="#fff" stroke-width="2" stroke-linecap="round" stroke-linejoin="round"><path d="M5 3h4l2 5-3 2a11 11 0 0 0 6 6l2-3 5 2v4a2 2 0 0 1-2 2A17 17 0 0 1 3 5a2 2 0 0 1 2-2z"/></svg>
        </span>
        <span class="contact-text">+972 4 555 0142</span>
      </li>
      <li class="contact">
        <span class="contact-icon">
          <svg width="15" height="15" viewBox="0 0 24 24" fill="none" stroke="#fff" stroke-width="2" stroke-linejoin="round"><rect x="3" y="5" width="18" height="14" rx="2"/><path d="M3 7l9 6 9-6"/></svg>
        </span>
        <span class="contact-text">ori@zip-wheel.co.il</span>
      </li>
      <li class="contact">
        <span class="contact-icon">
          <svg width="15" height="15" viewBox="0 0 24 24" fill="none" stroke="#fff" stroke-width="2"><circle cx="12" cy="12" r="9"/><path d="M3 12h18M12 3c3 3 3 15 0 18M12 3c-3 3-3 15 0 18"/></svg>
        </span>
        <span class="contact-text">zip-wheel.co.il</span>
      </li>
      <li class="contact">
        <span class="contact-icon">
          <svg width="15" height="15" viewBox="0 0 24 24" fill="#fff"><path d="M12 2a7 7 0 0 0-7 7c0 5 7 13 7 13s7-8 7-13a7 7 0 0 0-7-7zm0 9.5A2.5 2.5 0 1 1 12 6.5a2.5 2.5 0 0 1 0 5z"/></svg>
        </span>
        <span class="contact-text" dir="rtl">הדקל 42, חיפה</span>
      </li>
    </ul>
  </section>

</body>
</html>
```